Business card design incorporating discount offer

We are a trade services company and we need a double sided business card that is going to be used by our tradesmen to give to customers on completion of their jobs.

Below are the key elements of the card that we would like to include:

-Main logo with text 'Expert Property Care' underneath.
-Up to 12 smaller icon logos with text 'Your local all-trade experts' to emphasise the point that we cover all the trades
-Discount offer - 10% discount
-Telephone number and website address
-Blank space for tradesman to enter his/her name
-Request for customer feedback with feedback url

This business card will be printed on regular card. In the past we have favoured designs that use a black background but we're open to new ideas.

I have attached a few files:

-A simple wire frame example to show how this card could look with the different elements mentioned above, feel free to use a layout similar to this or come up with something totally different (biz-card.pdf)
-Front and back of a loyalty card the we've used in the past (this card was printed on plastic)
-Front and back of a key fob design that we've previously used (this card was printed on plastic)
-A logo file with the 12 small icons and the main logo image

If you need further images or information please ask.

```html
<!DOCTYPE html>
<html lang="en">
<head>
<meta charset="utf-8">
<title>HVT Business Card Options</title>
<link rel="stylesheet" href="https://fonts.googleapis.com/css2?family=Figtree:wght@300;400;500;600;700;800&display=swap">
<style>
  :root{
    --brand-blue:#0a7dc4;
    --icon-navy:#0f4c7e;
    --glyph-light:#d8edfb;
    --ink:#111111;
    --contact-grey:#4a4a4a;
    --caption-grey:#5a5a5a;
    --heading-navy:#1c2a4a;
    --card-white:#ffffff;
    --card-edge:#d9d9d9;
    --page:#ffffff;
  }
  *{margin:0;padding:0;box-sizing:border-box}
  html,body{width:1200px;height:900px;overflow:hidden;background:var(--page)}
  body{position:relative;font-family:"Figtree",Arial,sans-serif;color:var(--ink)}

  .option-title{position:absolute;left:27px;font-size:31px;font-weight:400;color:var(--heading-navy);letter-spacing:.2px}
  .option-title.first{top:8px}
  .option-title.second{top:454px}

  .card{position:absolute;width:570px;height:325px;border-radius:18px;overflow:hidden}
  .card.front{left:22px;background:var(--card-white);border:1px solid var(--card-edge)}
  .card.back{left:608px;width:569px;background:var(--brand-blue);color:#fff}
  .row-one{top:53px}
  .row-two{top:504px}

  .side-caption{position:absolute;font-size:17px;font-weight:600;letter-spacing:.5px;color:var(--caption-grey);text-align:center;width:200px}
  .side-caption.front-cap{left:187px}
  .side-caption.back-cap{left:790px}
  .side-caption.row-one-cap{top:391px}
  .side-caption.row-two-cap{top:842px}

  .offer-shape{position:absolute;left:0;top:0}

  .brand-block{position:absolute;left:94px;top:116px;width:200px;text-align:center}
  .brand-name{display:flex;align-items:center;justify-content:center;gap:12px;font-size:46px;font-weight:800;color:var(--ink);line-height:1}
  .brand-square{width:34px;height:34px;background:var(--ink)}
  .brand-tagline{margin-top:16px;font-size:18.5px;font-weight:700;color:var(--ink);white-space:nowrap}

  .offer{position:absolute;right:18px;text-align:right;color:#fff}
  .offer-figure{font-weight:300;line-height:1}
  .offer-word{font-weight:600}
  .offer-sub{font-weight:400}
  .offer-note{position:absolute;right:18px;text-align:right;font-size:12.5px;line-height:18px;color:#fff}

  .contact{position:absolute;display:flex;align-items:center;font-size:19px;font-weight:300;color:var(--contact-grey)}
  .contact .web{color:var(--brand-blue)}
  .contact .divider{width:1px;height:12px;background:#bbb;margin:0 9px}
  .contact svg{margin-right:4px}

  .trade-list{position:absolute;list-style:none}
  .trade-list li{display:flex;align-items:center;height:49.5px;font-size:13px;font-weight:300;color:#eaf5fd}
  .trade-list svg{width:30px;height:30px;color:var(--icon-navy);margin-right:9px;flex:none}

  .trade-grid{position:absolute;list-style:none}
  .trade-grid li{position:absolute;width:90px;margin-left:-45px;text-align:center;font-size:12.5px;font-weight:300;color:#e6f3fc}
  .trade-grid .badge{display:block;width:38px;height:38px;margin:0 auto 4px;border-radius:50%;background:var(--icon-navy);color:var(--glyph-light);padding:8px}
  .trade-grid .badge svg{width:22px;height:22px;display:block}

  .back-copy{position:absolute;right:24px;text-align:right;color:#fff}
  .strapline{font-size:19px}
  .tradesman-label{font-size:11.5px}
  .tradesman-name{font-size:19px;font-weight:700;letter-spacing:.3px}
  .feedback-ask{font-size:12px;font-weight:700}
  .feedback-line{font-size:12.5px;line-height:18px}
</style>
</head>
<body>

<svg width="0" height="0" style="position:absolute" aria-hidden="true">
  <defs>
    <symbol id="icon-bath" viewBox="0 0 24 24"><rect x="4" y="5" width="2" height="7" fill="currentColor"/><rect x="3" y="4" width="6" height="2" rx="1" fill="currentColor"/><rect x="1" y="11" width="22" height="2" fill="currentColor"/><path d="M2 13h20v1a5 5 0 0 1-5 5H7a5 5 0 0 1-5-5z" fill="currentColor"/><rect x="5" y="19" width="2" height="2" fill="currentColor"/><rect x="17" y="19" width="2" height="2" fill="currentColor"/></symbol>
    <symbol id="icon-saw" viewBox="0 0 24 24"><polygon points="2,20 15,7 19,11 5,22" fill="currentColor"/><rect x="15" y="2" width="6" height="8" rx="2" transform="rotate(45 18 6)" fill="currentColor"/></symbol>
    <symbol id="icon-hammer" viewBox="0 0 24 24"><rect x="10.5" y="7" width="3" height="17" rx="1" transform="rotate(35 12 15)" fill="currentColor"/><rect x="10" y="2" width="11" height="5" rx="1" transform="rotate(35 15 4)" fill="currentColor"/></symbol>
    <symbol id="icon-pipe" viewBox="0 0 24 24"><path d="M5 3v9a7 7 0 0 0 14 0V7" fill="none" stroke="currentColor" stroke-width="4"/><rect x="2" y="2" width="6" height="3" fill="currentColor"/><rect x="16" y="4" width="6" height="3" fill="currentColor"/></symbol>
    <symbol id="icon-bolt" viewBox="0 0 24 24"><polygon points="14,1 5,14 11,14 8,23 19,9 13,9 16,1" fill="currentColor"/></symbol>
    <symbol id="icon-drop" viewBox="0 0 24 24"><path d="M12 2C12 2 5 11 5 15a7 7 0 0 0 14 0C19 11 12 2 12 2z" fill="currentColor"/></symbol>
    <symbol id="icon-flame" viewBox="0 0 24 24"><path d="M12 1c1 5 7 8 7 14a7 7 0 0 1-14 0c0-4 3-6 4-9 1 3 1 5 3 6 1-4 0-7 0-11z" fill="currentColor"/></symbol>
    <symbol id="icon-wrench" viewBox="0 0 24 24"><circle cx="10" cy="9" r="7" fill="currentColor"/><circle cx="10" cy="9" r="3" fill="var(--brand-blue)"/><rect x="12" y="12" width="4" height="11" rx="1.5" transform="rotate(-40 14 17)" fill="currentColor"/></symbol>
    <symbol id="icon-brush" viewBox="0 0 24 24"><rect x="3" y="13" width="9" height="9" rx="1" transform="rotate(45 7.5 17.5)" fill="currentColor"/><rect x="12" y="2" width="4" height="13" rx="2" transform="rotate(45 14 8)" fill="currentColor"/></symbol>
    <symbol id="icon-pest" viewBox="0 0 24 24"><circle cx="12" cy="12" r="9" fill="none" stroke="currentColor" stroke-width="2.5"/><circle cx="12" cy="12" r="3.5" fill="currentColor"/></symbol>
    <symbol id="icon-oven" viewBox="0 0 24 24"><rect x="2" y="2" width="20" height="20" rx="1.5" fill="currentColor"/><rect x="5" y="9" width="14" height="10" fill="var(--brand-blue)"/><rect x="5" y="4" width="3" height="2" fill="var(--brand-blue)"/><rect x="10" y="4" width="3" height="2" fill="var(--brand-blue)"/></symbol>
  </defs>
</svg>

<!-- Option 01 -->
<h2 class="option-title first">Option-01</h2>

<section class="card front row-one">
  <svg class="offer-shape" width="570" height="325" aria-hidden="true"><path d="M493 0 Q280 162 498 325 L570 325 L570 0 Z" fill="var(--brand-blue)"/></svg>
  <div class="brand-block">
    <div class="brand-name"><span class="brand-square"></span>HVT</div>
    <div class="brand-tagline">Expert Property Care</div>
  </div>
  <div class="offer" style="top:74px">
    <div class="offer-figure" style="font-size:68px">10%</div>
    <div class="offer-word" style="font-size:27px;margin-top:2px">Discount</div>
    <div class="offer-sub" style="font-size:14.5px;margin-top:2px">With This Card</div>
  </div>
  <p class="offer-note" style="top:235px">Check our website for<br>full offer details</p>
  <div class="contact" style="left:44px;top:285px">
    <span>0800 000 1234</span><span class="divider"></span><span class="web">hvt-services.co.uk</span>
  </div>
</section>

<section class="card back row-one">
  <ul class="trade-list" style="left:26px;top:15px">
    <li><svg><use href="#icon-bath"/></svg>Bathrooms</li>
    <li><svg><use href="#icon-saw"/></svg>Carpentry</li>
    <li><svg><use href="#icon-hammer"/></svg>Building</li>
    <li><svg><use href="#icon-pipe"/></svg>Drainage</li>
    <li><svg><use href="#icon-bolt"/></svg>Electricians</li>
    <li style="font-size:14.5px"><svg><use href="#icon-oven"/></svg>Kitchen</li>
  </ul>
  <ul class="trade-list" style="left:150px;top:43px">
    <li><svg><use href="#icon-wrench"/></svg>Carpentry</li>
    <li><svg><use href="#icon-brush"/></svg>Painting</li>
    <li><svg><use href="#icon-pest"/></svg>Drainage</li>
    <li><svg><use href="#icon-drop"/></svg>Electricians</li>
    <li><svg><use href="#icon-flame"/></svg>Gas-Heating</li>
  </ul>
  <div class="back-copy" style="top:78px">
    <p class="strapline">Yourlocalall-tradeexperts</p>
    <p class="tradesman-label" style="margin-top:38px">YourHVT tradesman:</p>
    <p class="tradesman-name">Tradesman</p>
    <p class="feedback-line" style="margin-top:24px">Pleaseleavefeedbackonline</p>
    <p class="feedback-line">www.hvt-services.co.uk/feedback</p>
  </div>
</section>

<p class="side-caption front-cap row-one-cap">FRONT</p>
<p class="side-caption back-cap row-one-cap">BACK</p>

<!-- Option 02 -->
<h2 class="option-title second">Option-02</h2>

<section class="card front row-two">
  <svg class="offer-shape" width="570" height="325" aria-hidden="true"><path d="M468 0 L403 150 Q401 160 404 170 L448 325 L570 325 L570 0 Z" fill="var(--brand-blue)"/></svg>
  <div class="brand-block">
    <div class="brand-name"><span class="brand-square"></span>HVT</div>
    <div class="brand-tagline">Expert Property Care</div>
  </div>
  <div class="offer" style="top:48px">
    <div class="offer-figure" style="font-size:104px;letter-spacing:-2px;margin-right:-4px">10</div>
    <div class="offer-sub" style="font-size:13px;letter-spacing:2px;margin-top:2px">Percentage</div>
    <div class="offer-word" style="font-size:22px">Discount</div>
    <div class="offer-sub" style="font-size:14.5px">With This Card</div>
  </div>
  <p class="offer-note" style="top:237px">Check our website for<br>full offer details</p>
  <div class="contact" style="left:30px;top:281px">
    <svg width="12" height="16" viewBox="0 0 12 16" aria-hidden="true"><path d="M3 1 L6 1 L6 5 L4 6 Q4 10 6 11 L8 10 L10 14 L7 15 Q1 13 1 7 Q1 2 3 1z" fill="var(--brand-blue)"/></svg>
    <span>0800 000 1234</span>
    <svg width="14" height="14" viewBox="0 0 14 14" style="margin-left:22px" aria-hidden="true"><g fill="none" stroke="var(--brand-blue)" stroke-width="1.3"><circle cx="7" cy="7" r="6"/><ellipse cx="7" cy="7" rx="2.6" ry="6"/><line x1="1" y1="7" x2="13" y2="7"/></g></svg>
    <span>hvt-services.co.uk</span>
  </div>
</section>

<section class="card back row-two">
  <ul class="trade-grid" style="left:0;top:0">
    <li style="left:59px;top:19px"><span class="badge"><svg><use href="#icon-bath"/></svg></span>Bathrooms</li>
    <li style="left:150px;top:19px"><span class="badge"><svg><use href="#icon-hammer"/></svg></span>Building</li>
    <li style="left:241px;top:19px"><span class="badge"><svg><use href="#icon-saw"/></svg></span>Carpentry</li>
    <li style="left:332px;top:19px"><span class="badge"><svg><use href="#icon-pipe"/></svg></span>Drainage</li>
    <li style="left:424px;top:19px"><span class="badge"><svg><use href="#icon-bolt"/></svg></span>Electricians</li>
    <li style="left:515px;top:19px"><span class="badge"><svg><use href="#icon-drop"/></svg></span>Plumbing</li>
    <li style="left:93px;top:86px"><span class="badge"><svg><use href="#icon-flame"/></svg></span>Gas-Heating</li>
    <li style="left:189px;top:86px"><span class="badge"><svg><use href="#icon-wrench"/></svg></span>Handyman</li>
    <li style="left:286px;top:86px"><span class="badge"><svg><use href="#icon-brush"/></svg></span>Painting</li>
    <li style="left:383px;top:86px"><span class="badge"><svg><use href="#icon-pest"/></svg></span>Pest-Control</li>
    <li style="left:480px;top:86px"><span class="badge"><svg><use href="#icon-oven"/></svg></span>Kitchen</li>
  </ul>
  <div class="back-copy" style="top:165px">
    <p class="strapline" style="font-weight:300;font-size:20px">Yourlocalall-tradeexperts</p>
    <p class="tradesman-label" style="margin-top:12px;font-size:10px">YourHVT tradesman:</p>
    <p class="tradesman-name">Tradesman</p>
    <p class="feedback-ask" style="margin-top:14px">What do you think of our service?</p>
    <p class="feedback-line" style="margin-top:4px">Pleaseleavefeedbackonline</p>
    <p class="feedback-line">www.hvt-services.co.uk/feedback</p>
  </div>
</section>

<p class="side-caption front-cap row-two-cap">FRONT</p>
<p class="side-caption back-cap row-two-cap">BACK</p>

</body>
</html>
```